Stonebell Inc Ad Design, trying to attract new customers

Please see attached pictures and files for information
We are a Class A - Residential General Contractor in Millbrook, NC with Master HVAC and Master PLUMBING Licenses. We focus on Water and Air Solutions for property owners.
We build, remodel, and repair homes
We do HVAC, including Humidity Control and Air Purification
We do Plumbing
We love to fix Water Leaks for Plumbing, Roof Leaks, Skylight Leaks, Basement Leaks, Foundation Leaks, Door and Window Leaks
We solve water and air issues on the outside of properties with custom structures, grading, and landscaping

Target Market(s)

Residential and Light Commercial property owners

Industry/Entity Type

Construction

Font styles to use
Other font styles liked:
• see cards

Colors
0054AA
0677BA
7BADD7
CADEEF
E8F1F8
00AB8E
00BBA5
67D7C9
C6EFE9
E9F9F6

Requirements
Must have
• See business cards
Nice to have
• see business cards
Should not have
• My name

```html
<!DOCTYPE html>
<html lang="en">
<head>
<meta charset="utf-8">
<title>Stonebell Inc – Water &amp; Air Solutions Billboard</title>
<link rel="stylesheet" href="https://fonts.googleapis.com/css2?family=Anton&family=Montserrat:wght@700;800&family=Questrial&display=swap">
<style>
  :root{
    --page:#f4f6f8;
    --panel:#232323;
    --paper:#ffffff;
    --green-deep:#17793a;
    --green-light:#7cb940;
    --blue:#1b8ccc;
    --blue-deep:#1467a8;
    --blue-text:#1f84c6;
  }
  *{margin:0;padding:0;box-sizing:border-box}
  html,body{width:1200px;height:1121px;overflow:hidden;background:var(--page)}
  .billboard{
    position:absolute;left:40px;top:396px;width:1120px;height:328px;
    box-shadow:0 8px 18px rgba(0,0,0,.25);overflow:hidden;background:var(--paper);
  }
  .billboard__shapes{position:absolute;inset:0}
  .headline{
    position:absolute;left:34px;top:24px;
    font-family:"Anton",sans-serif;font-size:70px;line-height:1;letter-spacing:-1px;
    background:linear-gradient(90deg,var(--green-deep) 0%,var(--green-light) 45%,var(--green-deep) 100%);
    -webkit-background-clip:text;background-clip:text;color:transparent;
    transform:scaleY(1.05);transform-origin:left top;white-space:nowrap;
  }
  .services-line{
    position:absolute;left:34px;top:102px;
    font-family:"Montserrat",sans-serif;font-weight:800;font-size:41px;line-height:1;
    letter-spacing:1.5px;white-space:nowrap;
    background:linear-gradient(90deg,var(--blue) 0%,var(--blue-deep) 100%);
    -webkit-background-clip:text;background-clip:text;color:transparent;
  }
  .rule{position:absolute;left:35px;top:154px;width:370px;height:3px;background:var(--green-deep)}
  .credential{
    position:absolute;left:35px;top:166px;
    font-family:"Questrial",sans-serif;font-size:18px;color:var(--blue-text);white-space:nowrap;
  }
  .checklist{
    position:absolute;left:35px;top:194px;display:flex;gap:8px;list-style:none;
    font-family:"Questrial",sans-serif;font-size:24px;color:#fff;white-space:nowrap;
  }
  .checklist li{display:flex;align-items:center;gap:3px}
  .checklist svg{width:22px;height:22px}
  .brand{
    position:absolute;left:28px;top:268px;display:flex;align-items:center;gap:8px;
    font-family:"Montserrat",sans-serif;font-weight:800;font-size:22px;color:var(--blue-deep);
    letter-spacing:.5px;white-space:nowrap;
  }
  .brand__dot{width:14px;height:14px;border-radius:50%;background:var(--green-light)}
  .contact{position:absolute;left:270px;top:244px}
  .contact__row{display:flex;align-items:center;gap:6px;white-space:nowrap}
  .contact__phone{
    font-family:"Montserrat",sans-serif;font-weight:800;font-size:43px;line-height:1.02;letter-spacing:1px;
    background:linear-gradient(90deg,var(--green-deep),var(--green-light) 50%,var(--green-deep));
    -webkit-background-clip:text;background-clip:text;color:transparent;
  }
  .contact__web{font-family:"Questrial",sans-serif;font-size:32px;line-height:1.05;color:var(--blue-text)}
  .contact svg{flex:none}
</style>
</head>
<body>
<section class="billboard" aria-label="Stonebell Inc billboard">
  <svg class="billboard__shapes" viewBox="0 0 1120 328" width="1120" height="328">
    <defs>
      <linearGradient id="photoTones" x1="0" y1="0" x2="0" y2="1">
        <stop offset="0" stop-color="#cfe2f2"/>
        <stop offset=".3" stop-color="#e6d49c"/>
        <stop offset=".55" stop-color="#d6b46a"/>
        <stop offset=".78" stop-color="#6f9c3c"/>
        <stop offset="1" stop-color="#4e7b2b"/>
      </linearGradient>
    </defs>
    <rect class="panel" x="0" y="0" width="1120" height="239" fill="#232323"/>
    <rect class="band" x="0" y="239" width="1120" height="89" fill="#ffffff"/>
    <path role="img" aria-label="Photo of a yellow craftsman bungalow with white porch, front steps and green lawn"
      d="M745,0 C770,40 760,90 748,130 C735,175 730,220 738,260 C745,295 752,315 760,328 L1120,328 L1120,0 Z"
      fill="url(#photoTones)"/>
    <path d="M728,0 C755,40 748,90 736,130 C722,175 716,220 724,260 C730,295 738,315 745,328 L760,328 C752,315 745,295 738,260 C730,220 735,175 748,130 C760,90 770,40 745,0 Z" fill="#1b6fae"/>
    <path d="M708,0 C732,35 734,85 718,140 C744,88 744,35 724,0 Z" fill="#1b8ccc"/>
    <path d="M258,241 C248,270 248,300 256,328" fill="none" stroke="#1b8ccc" stroke-width="3"/>
  </svg>

  <h1 class="headline">WATER &amp; AIR SOLUTIONS</h1>
  <p class="services-line">BUILD ▪ REMODEL ▪ REPAIR</p>
  <div class="rule"></div>
  <p class="credential">Class A Residential Contractor — Millbrook, NC</p>
  <ul class="checklist">
    <li><svg viewBox="0 0 22 22"><rect x="2" y="4" width="15" height="15" rx="2" fill="none" stroke="#1f84c6" stroke-width="2.4"/><path d="M6 11 l4 4 L20 3" fill="none" stroke="#1f84c6" stroke-width="2.8"/></svg>HVAC</li>
    <li><svg viewBox="0 0 22 22"><rect x="2" y="4" width="15" height="15" rx="2" fill="none" stroke="#1f84c6" stroke-width="2.4"/><path d="M6 11 l4 4 L20 3" fill="none" stroke="#1f84c6" stroke-width="2.8"/></svg>Plumbing</li>
    <li><svg viewBox="0 0 22 22"><rect x="2" y="4" width="15" height="15" rx="2" fill="none" stroke="#1f84c6" stroke-width="2.4"/><path d="M6 11 l4 4 L20 3" fill="none" stroke="#1f84c6" stroke-width="2.8"/></svg>Leaks</li>
    <li><svg viewBox="0 0 22 22"><rect x="2" y="4" width="15" height="15" rx="2" fill="none" stroke="#1f84c6" stroke-width="2.4"/><path d="M6 11 l4 4 L20 3" fill="none" stroke="#1f84c6" stroke-width="2.8"/></svg>Custom Exteriors</li>
  </ul>

  <div class="brand"><span class="brand__dot"></span>Stonebell Inc</div>

  <div class="contact">
    <div class="contact__row">
      <svg width="24" height="24" viewBox="0 0 24 24"><path d="M6.6 10.8c1.4 2.8 3.8 5.1 6.6 6.6l2.2-2.2c.3-.3.7-.4 1-.2 1.1.4 2.3.6 3.6.6.6 0 1 .4 1 1V20c0 .6-.4 1-1 1C10.6 21 3 13.4 3 4c0-.6.4-1 1-1h3.5c.6 0 1 .4 1 1 0 1.3.2 2.5.6 3.6.1.3 0 .7-.2 1z" fill="#17793a"/></svg>
      <span class="contact__phone">(555) 014-2290</span>
    </div>
    <div class="contact__row">
      <svg width="22" height="22" viewBox="0 0 24 24" fill="none" stroke="#1f84c6" stroke-width="2"><circle cx="12" cy="12" r="9"/><ellipse cx="12" cy="12" rx="4" ry="9"/><path d="M3 12h18M5 7h14M5 17h14"/></svg>
      <span class="contact__web">stonebellconstruction.com</span>
    </div>
  </div>
</section>
</body>
</html>
```